Sundial Bail Bonds Signboard Ad

I need a signboard ad that will be posted at a jail. We are a bail bond company and we bail people out of jail. The inmate/customer will call our company when they see our signboard ad posted inside a jail. The goal of the signboard ad is to get the attention of a person in custody and to stand out from the competition. The signboard ad is about 5x7. Open to any colors that will make it stand out. The content of the signboard ad must have "Sundial Bail Bonds" and our company phone number: (555) 318-2746. We want to emphasize we can get them out of jail quick and fast, was thinking maybe a catch phrase of "Sundial outta Jail" or "Sundial to Freedom". We don't have a logo. I will upload an attachment to show what the competition looks like. As you will see in the upload, my ad will go along with my competition. Also, I'm open to any creative ideas that will make my signboard ad stand out. Thank You.

Target Market(s)

People in jail.

Requirements
Must have
• Sundial Bail Bonds

(555) 318-2746
Nice to have
• I'm open to catch phrases that will get attention, for example "Sundial outta Jail" or "Sundial to Freedom". I do not have a company logo, if you can create a company logo, would be nice, was thinking an image of a rocket blasting off, The name of company is Sundial Bail Bonds.

```html
<!DOCTYPE html>
<html lang="en">
<head>
<meta charset="utf-8">
<title>Sundial Bail Bonds Signboard</title>
<link rel="stylesheet" href="https://fonts.googleapis.com/css2?family=Kaushan+Script&family=Quicksand:wght@700&family=Arimo:wght@400;700&display=swap">
<style>
  :root {
    --sign-white: #ffffff;
    --ink-black: #000000;
    --signal-yellow: #f3ea14;
    --brand-red: #e31c3d;
  }
  * { margin: 0; padding: 0; box-sizing: border-box; }
  html, body {
    width: 1200px;
    height: 857px;
    overflow: hidden;
    background: var(--sign-white);
  }
  .signboard {
    position: relative;
    width: 1200px;
    height: 857px;
    background: var(--sign-white);
  }
  .trim {
    position: absolute;
    left: 16px;
    right: 16px;
    height: 12px;
    background: var(--brand-red);
  }
  .trim--top { top: 8px; }
  .trim--bottom { top: 836px; }
  .headline-band {
    position: absolute;
    left: 16px;
    right: 16px;
    top: 22px;
    height: 278px;
    background: var(--ink-black);
    display: flex;
    align-items: center;
    justify-content: center;
  }
  .headline {
    font-family: "Kaushan Script", cursive;
    font-weight: 400;
    font-size: 112px;
    color: var(--sign-white);
    white-space: nowrap;
    line-height: 1;
  }
  .phone-band {
    position: absolute;
    left: 16px;
    right: 16px;
    top: 300px;
    height: 260px;
    background: var(--signal-yellow);
    display: flex;
    align-items: center;
    justify-content: center;
  }
  .phone-number {
    font-family: "Quicksand", sans-serif;
    font-weight: 700;
    font-size: 150px;
    color: var(--ink-black);
    letter-spacing: 1px;
    white-space: nowrap;
    line-height: 1;
  }
  .intro-pill {
    position: absolute;
    left: 0;
    top: 655px;
    width: 350px;
    height: 105px;
    background: var(--signal-yellow);
    border-radius: 0 52px 52px 0;
    display: flex;
    align-items: center;
    justify-content: flex-end;
    padding-right: 38px;
  }
  .intro-text {
    font-family: "Arimo", sans-serif;
    font-weight: 400;
    font-size: 60px;
    color: var(--ink-black);
    line-height: 1;
  }
  .company-name {
    position: absolute;
    left: 430px;
    top: 615px;
    width: 720px;
    height: 180px;
    display: flex;
    align-items: center;
    gap: 30px;
  }
  .company-mark {
    flex: none;
    width: 120px;
    height: 120px;
  }
  .company-title {
    font-family: "Arimo", sans-serif;
    font-weight: 700;
    font-size: 78px;
    line-height: 0.95;
    color: var(--brand-red);
  }
</style>
</head>
<body>
  <main class="signboard">
    <div class="trim trim--top"></div>

    <section class="headline-band">
      <h1 class="headline">Sundial outta Jail!</h1>
    </section>

    <section class="phone-band">
      <p class="phone-number">(555)318-2746</p>
    </section>

    <div class="intro-pill">
      <span class="intro-text">We are</span>
    </div>

    <div class="company-name">
      <svg class="company-mark" viewBox="0 0 120 120" aria-hidden="true">
        <circle cx="60" cy="60" r="56" fill="var(--brand-red)"/>
      </svg>
      <p class="company-title">Sundial<br>Bail Bonds</p>
    </div>

    <div class="trim trim--bottom"></div>
  </main>
</body>
</html>
```